Speisekarten-Design für Tennis- und Freizeitanlage mit Restaurant und Biergarten
Zielgruppe
Tennis- und Freizeitanlage mit Restaurant und Biergarten. Zielgruppe von Jung bis Alt
Aufgabenstellung
Speise- und Getränkekarte. Klassisch und klar strukturiert. Möglichst zum selbst ausdrucken (kein Randloses Design) Möglichkeit zum selbstständigen ändern als Word Dokument. A4 Format. Hülle der Speisekarte bereits vorhanden. Siehe Fotos
Wenn möglich farbiges Logo verwenden. Alternativ habe ich noch eine schwarz weiß Variante hinzugefügt.

```html
<!DOCTYPE html>
<html lang="de">
<head>
<meta charset="utf-8">
<title>Speisekarte – Tennis Lindenhof</title>
<link href="https://fonts.googleapis.com/css2?family=Source+Serif+4:opsz,wght@8..60,400;8..60,500&family=Inter:wght@400&display=swap" rel="stylesheet">
<style>
  :root {
    --backdrop: #355a48;
    --paper: #f2f0ea;
    --mint: #c3dccb;
    --green: #2f5e46;
    --line: #4a7a60;
    --clay: #c9633a;
    --lime: #bfc62e;
  }
  html, body {
    margin: 0;
    padding: 0;
    width: 1200px;
    height: 900px;
    overflow: hidden;
    background: var(--backdrop);
  }
  .canvas {
    position: relative;
    width: 1200px;
    height: 900px;
  }
  .page {
    position: absolute;
    top: 107px;
    width: 441px;
    height: 685px;
    background: var(--paper);
    overflow: hidden;
  }
  .page--back { left: 133px; }
  .page--cover { left: 626px; }

  .page__band {
    position: absolute;
    left: 0;
    right: 0;
    background: var(--mint);
  }
  .page--back .page__band { top: 192px; height: 303px; }
  .page--cover .page__band { top: 241px; bottom: 0; border-top: 1px solid var(--line); }

  .page__frame {
    position: absolute;
    inset: 0;
    width: 441px;
    height: 685px;
    pointer-events: none;
    z-index: 3;
  }

  .club-name {
    position: absolute;
    left: 0;
    right: 0;
    display: flex;
    align-items: center;
    justify-content: center;
    gap: 8px;
    font-family: "Source Serif 4", Georgia, serif;
    font-weight: 500;
    color: var(--green);
    z-index: 2;
  }
  .club-name__mark {
    background: var(--clay);
  }
  .page--back .club-name { top: 96px; font-size: 17px; }
  .page--back .club-name__mark { width: 12px; height: 12px; }
  .page--cover .club-name { top: 128px; font-size: 28px; }
  .page--cover .club-name__mark { width: 18px; height: 18px; }

  .court-photo {
    position: absolute;
    left: 92px;
    top: 244px;
    width: 257px;
    height: 198px;
    background: linear-gradient(180deg, #8fb3d6 0%, #4d7a3e 28%, #2f5a3c 44%, #c4623a 48%, #b5542f 100%);
    z-index: 2;
  }

  .venue-info {
    position: absolute;
    left: 0;
    right: 0;
    top: 565px;
    text-align: center;
    font-family: "Inter", Arial, sans-serif;
    font-size: 12.5px;
    line-height: 16px;
    color: var(--green);
    z-index: 2;
  }
  .venue-info p { margin: 0; }
  .venue-info .venue-info__address { margin-top: 15px; }

  .menu-title {
    position: absolute;
    left: 0;
    right: 0;
    top: 290px;
    margin: 0;
    text-align: center;
    font-family: "Source Serif 4", Georgia, serif;
    font-weight: 500;
    font-size: 50px;
    letter-spacing: 0.5px;
    color: var(--green);
    z-index: 2;
  }
  .menu-title__rule {
    position: absolute;
    left: 158px;
    top: 374px;
    width: 125px;
    height: 1px;
    background: var(--line);
    z-index: 2;
  }

  .tennis-motif {
    position: absolute;
    left: 0;
    right: 0;
    top: 433px;
    bottom: 0;
    background: linear-gradient(90deg, var(--lime) 0%, #c7d27a 28%, var(--mint) 45%, var(--mint) 62%, #c7d27a 74%, var(--lime) 100%);
    z-index: 1;
  }
</style>
</head>
<body>
<main class="canvas">

  <section class="page page--back">
    <div class="page__band"></div>
    <div class="club-name"><span class="club-name__mark"></span>Lindenhof</div>
    <div class="court-photo" role="img" aria-label="Foto eines Sandplatzes mit Netz, umgeben von Bäumen unter blauem Himmel"></div>
    <div class="venue-info">
      <p>Tennis Lindenhof</p>
      <p>Restaurant und Biergarten</p>
      <p class="venue-info__address">Am Park im Garten</p>
    </div>
    <svg class="page__frame" viewBox="0 0 441 685" aria-hidden="true">
      <path d="M33 19 H408 A14 14 0 0 0 422 33 V652 A14 14 0 0 0 408 666 H33 A14 14 0 0 0 19 652 V33 A14 14 0 0 0 33 19 Z" fill="none" stroke="#4a7a60" stroke-width="1.2"/>
      <path d="M35 25 H406 A10 10 0 0 0 416 35 V650 A10 10 0 0 0 406 660 H35 A10 10 0 0 0 25 650 V35 A10 10 0 0 0 35 25 Z" fill="none" stroke="#4a7a60" stroke-width="1.2"/>
    </svg>
  </section>

  <section class="page page--cover">
    <div class="page__band"></div>
    <div class="club-name"><span class="club-name__mark"></span>Lindenhof</div>
    <h1 class="menu-title">Speisekarte</h1>
    <div class="menu-title__rule"></div>
    <div class="tennis-motif" role="img" aria-label="Illustration: zwei Tennisbälle vor einem Tennisnetz"></div>
    <svg class="page__frame" viewBox="0 0 441 685" aria-hidden="true">
      <path d="M33 19 H408 A14 14 0 0 0 422 33 V652 A14 14 0 0 0 408 666 H33 A14 14 0 0 0 19 652 V33 A14 14 0 0 0 33 19 Z" fill="none" stroke="#4a7a60" stroke-width="1.2"/>
      <path d="M35 25 H406 A10 10 0 0 0 416 35 V650 A10 10 0 0 0 406 660 H35 A10 10 0 0 0 25 650 V35 A10 10 0 0 0 35 25 Z" fill="none" stroke="#4a7a60" stroke-width="1.2"/>
    </svg>
  </section>

</main>
</body>
</html>
```